Business software developers new website

We need to redesign our website. Our current website is http://www.quorvanta.net/index.html, which is outdated and needs a new look. We moved out from web design and have concentrated more on the back end of the systems, for example, system support and security and cloud-based applications. Our major clients include both private and government sectors. We would like to see some designs that are all in one page, simple and clean. Prefer illustrator or obstructed images instead of real-life photos. Must look futuristic yet friendly. Attached the new logo for your references and good luck.

Target Market(s)

Medium to big company for their IT or data management. Either improve or upgrade their current system.

Industry/Entity Type

Business Software

Number of Pages Required

1 page

Colors

Designer to choose colors to be used in the design.

Requirements
Must have
• Simple and clean. Individual assets must be provided in the correct size and format(png or jpeg). Prefer Goggle fonts. Even though the logo color is red, grey and black, still prefer some modern colors that go well with red. When design, must consider the possibility to convert it into responsive.
Nice to have
• White background
Should not have
• real life photos, no slider

```html
<!DOCTYPE html>
<html lang="en">
<head>
<meta charset="utf-8">
<title>quorvanta.net – Business Software, Support &amp; Cloud</title>
<link rel="stylesheet" href="https://fonts.googleapis.com/css2?family=Titillium+Web:wght@300;400;600&family=Open+Sans:wght@400;600&display=swap">
<style>
:root{
  --red:#e8323c;
  --ink:#222;
  --text:#444;
  --muted:#888;
  --band:#f6f6f9;
  --purple:#8e44ad;
  --violet:#6a5fd0;
  --blue:#4a80e2;
  --magenta:#d13aa6;
  --pink:#ef5080;
  --btn-grey:#ececec;
  --footer:#3b3b3d;
  --line:#dcdcdc;
  --grad:linear-gradient(90deg,#8e44ad,#5b6fe0);
}
*{box-sizing:border-box;margin:0;padding:0}
html,body{width:1200px;height:3567px;overflow:hidden}
body{position:relative;background:#fff;font-family:"Titillium Web",sans-serif;color:var(--text)}
.abs{position:absolute}
.center{left:0;width:1200px;text-align:center}

/* header */
.logo{left:144px;top:20px;font-size:34px;font-weight:400;color:var(--ink);display:flex;align-items:center;gap:8px;letter-spacing:.5px;line-height:46px}
.logo-mark{width:14px;height:14px;background:var(--red)}
.nav{right:145px;top:31px;display:flex;gap:31px;font-size:14px;color:#555;line-height:20px}
.nav .active{color:var(--red)}

/* hero */
.hero-art{left:400px;top:86px}
.hero-copy{left:144px;top:190px;width:352px;font-size:21px;line-height:34px;color:var(--ink);font-weight:300}
.hero-copy em{font-style:normal;color:var(--red)}
.phone{left:144px;width:199px;height:43px;border-radius:22px;background:#eee;display:flex;align-items:center;font-size:15px;color:var(--ink);font-weight:400}
.phone .ico{width:40px;height:43px;display:flex;align-items:center;justify-content:center;border-right:1px solid #ddd;margin-right:13px}

/* sections */
.band{left:0;width:1200px;background:var(--band)}
.wave{left:0}
.h2{font-size:41px;color:var(--red);font-weight:600;line-height:1}
.lead{left:150px;width:900px;font-family:"Open Sans",sans-serif;font-size:14px;line-height:26px;color:#555;text-align:center}
.btn{height:34px;border-radius:17px;font-size:12px;display:flex;align-items:center;justify-content:center;text-transform:uppercase;font-family:"Open Sans",sans-serif}
.btn-grad{background:var(--grad);color:#fff;width:96px;left:552px}
.btn-grey{background:var(--btn-grey);color:#555;width:96px}

.card{width:300px;text-align:center}
.card .icon{width:96px;height:96px;border-radius:22px;margin:0 auto;display:flex;align-items:center;justify-content:center}
.card h3{font-size:19px;font-weight:600;margin-top:12px;line-height:24px}
.card p{font-family:"Open Sans",sans-serif;font-size:10.5px;line-height:17px;color:var(--muted);margin-top:8px;height:52px}
.card .btn{margin:6px auto 0}

.shot{top:2054px;width:297px;height:342px;border:1px solid #ddd}

.faq-q{font-size:21px;color:var(--ink);font-weight:400;line-height:28px}
.faq-a{left:150px;width:900px;font-family:"Open Sans",sans-serif;font-size:11.5px;line-height:19px;color:#555;text-align:center}
.rule{left:144px;width:911px;height:1px;background:var(--line)}

.field{height:40px;border:1px solid #d6d6d6;background:#fff;font-family:"Open Sans",sans-serif;font-size:12px;color:#999;padding:12px 15px}

/* footer */
.footer{left:0;top:3468px;width:1200px;height:99px;background:var(--footer)}
.foot-links{left:144px;top:3496px;font-family:"Open Sans",sans-serif;font-size:11px;color:#ddd;display:flex;gap:10px}
.copy{left:144px;top:3524px;font-family:"Open Sans",sans-serif;font-size:11px;color:#ccc}
.social{top:3508px;width:16px;height:16px;border-radius:50%;background:#bbb}
</style>
</head>
<body>

<!-- header -->
<div class="abs logo"><span>quorvanta.net</span><span class="logo-mark"></span></div>
<nav class="abs nav"><span class="active">Home</span><span>About Us</span><span>Services</span><span>Portfolio</span><span>News</span><span>FAQ</span><span>Contact Us</span></nav>

<!-- hero -->
<svg class="abs hero-art" width="800" height="527" viewBox="400 86 800 527" role="img" aria-label="Illustration of a systems team working at laptops and large code screens on a blue-to-purple backdrop">
  <defs><linearGradient id="heroGrad" x1="0" y1="0" x2="1" y2="1"><stop offset="0" stop-color="#3f7fe0"/><stop offset="1" stop-color="#8a45b0"/></linearGradient></defs>
  <path d="M700 86H1200V613H640C560 560 515 410 555 270C585 170 640 110 700 86Z" fill="url(#heroGrad)"/>
</svg>
<p class="abs hero-copy">We are an Australian based Business Software Company that provides <em>system support, security and cloud-based applications</em> for clients worldwide.</p>
<div class="abs phone" style="top:386px"><span class="ico"><svg width="14" height="14" viewBox="0 0 24 24"><path d="M6.6 10.8a15 15 0 0 0 6.6 6.6l2.2-2.2a1 1 0 0 1 1-.25 11.4 11.4 0 0 0 3.6.57 1 1 0 0 1 1 1V20a1 1 0 0 1-1 1A17 17 0 0 1 3 4a1 1 0 0 1 1-1h3.5a1 1 0 0 1 1 1c0 1.25.2 2.45.57 3.57a1 1 0 0 1-.25 1z" fill="#e8323c"/></svg></span>+61 7 5550 1234</div>
<div class="abs phone" style="top:447px"><span class="ico"><svg width="12" height="16" viewBox="0 0 12 16"><rect x="1" y="1" width="10" height="14" rx="2" fill="none" stroke="#e8323c" stroke-width="2"/><rect x="5" y="11.5" width="2" height="1.5" fill="#e8323c"/></svg></span>+61 0400 555 018</div>

<!-- philosophy -->
<h2 class="abs center h2" style="top:688px">Our Philosophy</h2>
<p class="abs lead" style="top:742px">As software engineers, we understand that secure and reliable back-end systems are a vital component of every modern organisation, private or government. This is why our team works with all of our clients to improve or upgrade their current systems so their IT and data run smoothly.</p>
<div class="abs btn btn-grad" style="top:837px">Read more</div>

<!-- services band -->
<svg class="abs wave" style="top:895px" width="1200" height="110" viewBox="0 0 1200 110" preserveAspectRatio="none"><path d="M0 40C150 -10 300 10 450 45S750 90 900 40 1100 10 1200 35V110H0Z" fill="#f6f6f9"/></svg>
<div class="abs band" style="top:1004px;height:830px"></div>
<svg class="abs wave" style="top:1834px" width="1200" height="110" viewBox="0 0 1200 110" preserveAspectRatio="none"><path d="M0 0H1200V60C1100 100 950 90 800 55S500 15 350 60 100 100 0 70Z" fill="#f6f6f9"/></svg>

<h2 class="abs center h2" style="top:1056px">Works</h2>
<div class="abs card" style="left:139px;top:1135px">
  <div class="icon" style="background:var(--purple)"><svg width="48" height="46" viewBox="0 0 48 46" fill="none" stroke="#fff" stroke-width="2"><path d="M8 26v-4a16 16 0 0 1 32 0v4"/><rect x="4" y="24" width="8" height="12" rx="2"/><rect x="36" y="24" width="8" height="12" rx="2"/><path d="M40 36c0 5-5 7-12 7"/></svg></div>
  <h3 style="color:var(--purple)">System Support</h3>
  <p>Your systems need to run every hour of the day. Our support team monitors, maintains and fixes issues before they reach your users.</p>
  <div class="btn btn-grey">Read more</div>
</div>
<div class="abs card" style="left:449px;top:1135px">
  <div class="icon" style="background:var(--violet)"><svg width="50" height="44" viewBox="0 0 50 44" fill="none" stroke="#fff" stroke-width="2"><rect x="2" y="2" width="40" height="28" rx="2"/><path d="M16 40h12M22 30v10M14 12l-5 5 5 5M30 12l5 5-5 5M25 10l-6 14"/><circle cx="41" cy="33" r="6"/></svg></div>
  <h3 style="color:var(--violet)">Software Development</h3>
  <p>We build robust, reliable business software – and make sure it stays that way. We cover all your back-end needs, from data tools to integrations...</p>
  <div class="btn btn-grey">Read more</div>
</div>
<div class="abs card" style="left:759px;top:1135px">
  <div class="icon" style="background:var(--blue)"><svg width="52" height="40" viewBox="0 0 52 40" fill="none" stroke="#fff" stroke-width="2"><path d="M14 34h26a9 9 0 0 0 0-18 13 13 0 0 0-25-2A10 10 0 0 0 14 34z"/></svg></div>
  <h3 style="color:var(--blue)">Cloud Applications</h3>
  <p>We move your applications and data to the cloud, so your teams can reach them safely from anywhere and scale as you grow...</p>
  <div class="btn btn-grey">Read more</div>
</div>

<h2 class="abs center h2" style="top:1440px">Technology</h2>
<div class="abs card" style="left:139px;top:1518px">
  <div class="icon" style="background:var(--red)"><svg width="50" height="42" viewBox="0 0 50 42" fill="none" stroke="#fff" stroke-width="2"><rect x="2" y="2" width="46" height="38" rx="4"/><path d="M2 12h46"/><circle cx="8" cy="7" r="1.5"/><circle cx="14" cy="7" r="1.5"/><circle cx="20" cy="7" r="1.5"/><path d="M19 20l-5 6 5 6M31 20l5 6-5 6M27 18l-4 16"/></svg></div>
  <h3 style="color:var(--red)">Programming</h3>
  <p>We specialize in a variety of back-end languages and databases.</p>
  <div class="btn btn-grey">Read more</div>
</div>
<div class="abs card" style="left:449px;top:1518px">
  <div class="icon" style="background:var(--magenta)"><svg width="40" height="46" viewBox="0 0 40 46" fill="none" stroke="#fff" stroke-width="2.5"><path d="M20 3l15 6v12c0 11-7 18-15 22C12 39 5 32 5 21V9z"/><path d="M13 23l5 5 9-10"/></svg></div>
  <h3 style="color:var(--magenta)">System Security</h3>
  <p>All of our systems are built secure, so you never have to worry about breaches or data loss.</p>
  <div class="btn btn-grey">Read more</div>
</div>
<div class="abs card" style="left:759px;top:1518px">
  <div class="icon" style="background:var(--pink)"><svg width="46" height="46" viewBox="0 0 46 46" fill="none" stroke="#fff" stroke-width="2"><rect x="3" y="3" width="40" height="12" rx="2"/><rect x="3" y="17" width="40" height="12" rx="2"/><rect x="3" y="31" width="40" height="12" rx="2"/><circle cx="10" cy="9" r="2"/><circle cx="10" cy="23" r="2"/><circle cx="10" cy="37" r="2"/><path d="M24 9h12M24 23h12M24 37h12"/></svg></div>
  <h3 style="color:var(--pink)">Hosting Solutions</h3>
  <p>We offer competitive cloud hosting with all of our projects so you never have to worry about finding your data the right home.</p>
  <div class="btn btn-grey">Read more</div>
</div>

<!-- portfolio -->
<h2 class="abs center h2" style="top:1994px">Portfolio</h2>
<div class="abs shot" style="left:144px;background:linear-gradient(180deg,#45566a 0 4%,#eef0f1 4% 40%,#3cb3b5 40% 42%,#f1f1f1 42%)" role="img" aria-label="Project preview of a business dashboard with header and icon grid"></div>
<div class="abs shot" style="left:451px;background:linear-gradient(180deg,#f2f3f4 0 20%,#4f7d44 20% 40%,#9fb8a4 40% 70%,#e6e6e6 70%)" role="img" aria-label="Project preview of a client portal with banner and coloured tiles"></div>
<div class="abs shot" style="left:758px;background:linear-gradient(180deg,#2c3f66 0 6%,#6d8fd2 6% 30%,#d6def0 30% 60%,#f3f3f3 60%)" role="img" aria-label="Project preview of a wholesale system with banner and product icons"></div>
<div class="abs btn btn-grad" style="top:2425px">View all</div>

<!-- faq band -->
<svg class="abs wave" style="top:2495px" width="1200" height="110" viewBox="0 0 1200 110" preserveAspectRatio="none"><path d="M0 50C120 10 280 5 430 45S720 100 880 50 1100 15 1200 40V110H0Z" fill="#f6f6f9"/></svg>
<div class="abs band" style="top:2604px;height:395px"></div>
<svg class="abs wave" style="top:2999px" width="1200" height="110" viewBox="0 0 1200 110" preserveAspectRatio="none"><path d="M0 0H1200V55C1080 95 930 90 780 50S480 15 330 55 90 95 0 65Z" fill="#f6f6f9"/></svg>

<h2 class="abs center h2" style="top:2642px">FAQ</h2>
<div class="abs center faq-q" style="top:2705px">How much does a system upgrade by Quorvanta.net cost?</div>
<p class="abs faq-a" style="top:2740px">There are quite a few factors that are going to affect the ultimate cost of your upgrade. These factors include how many users you have, how much data you hold, whether you move to the cloud, and the level of support and security you need.</p>
<div class="abs rule" style="top:2798px"></div>
<div class="abs center faq-q" style="top:2825px">How long does it take to upgrade an existing system?</div>
<p class="abs faq-a" style="top:2860px">Again it all depends on the size of your current system, how much data has to be moved, the integrations involved, and the security checks your sector requires. Contact us for a free assessment.</p>
<div class="abs btn btn-grad" style="top:2918px">View all</div>

<!-- contact -->
<h2 class="abs center h2" style="top:3135px">Contact Us</h2>
<div class="abs field" style="left:144px;top:3193px;width:218px">Full name</div>
<div class="abs field" style="left:375px;top:3193px;width:218px">Company name</div>
<div class="abs field" style="left:606px;top:3193px;width:218px">Email</div>
<div class="abs field" style="left:837px;top:3193px;width:218px">Phone</div>
<div class="abs field" style="left:144px;top:3247px;width:911px;height:88px">Message</div>
<div class="abs btn btn-grad" style="top:3354px">Submit</div>

<!-- footer -->
<footer class="abs footer"></footer>
<div class="abs foot-links"><span>Home</span><span>|</span><span>About Us</span><span>|</span><span>Services</span><span>|</span><span>Portfolio</span><span>|</span><span>News</span><span>|</span><span>FAQ</span><span>|</span><span>Contact Us</span></div>
<div class="abs copy">Copyright © 2019 Quorvanta. All rights reserved.</div>
<span class="abs social" style="left:964px"></span>
<span class="abs social" style="left:998px"></span>
<span class="abs social" style="left:1037px"></span>

</body>
</html>
```